Alcohol Marketing website

Home page and information page design, details as follows

CLIENT PURPOSE
Increase online visibility and create good contacts to increase business.

SERVICES
Drinks Marketing Consultancy
Brand Representation
Spirit Brand Sales & Marketing
Brand Development
Brand Distribution
Brand Launch & Introductions

COMPETITION
hazelpour.co.uk -
quintaloft.co.uk -

WEBSITE(S) CLIENT LIKES
Small competitors I admire:
http://www.hazelpour.co.uk/main.htm
http://www.quintaloft.com
http://www.morvatide.co.uk/spiritsliqueursbybrand.php
http://www.kelbrowhouse.com/page1.html
http://www.quorrifenwave.co.uk/index.asp

Nice page layout:
http://www.nkplume.com/
http://www.wzoharbour.com/
http://www.pelvit.com/index.cfm?do=pelvit.home

WEBSITE CLIENT DOES NOT LIKE
http://www.corvanhall.com/
http://www.amberlode-hall.com/
http://www.thesupperfold.co.uk/aboutUs.html
http://www.grainandkettle.com/
http://www.tessmarrow.co.uk/default.asp
http://www.pinnock-halden.co.uk/start.htm
http://www.rilby.co.uk/
http://www.vmkettles.com/default2.aspx
http://www.tumbril-vale.co.uk/mainpage.aspx

COMPANY LOGO
Customer has a company logo (Supplied)

COLOURS:
Blue
White

STRAPLINE:
No

WEBSITE THEME: Marketing

IMAGES THAT BEST REFLECT THE COMPANY:
Spirits / Drinks

HEADER IMAGE:
Spirits / Brands

PAGES:
home
strength& flavour
a little about us
our spirit marketing
big brand success
speak to us

USER JOURNEYS:
General Service > Land on website >Navigation > Info Pages > Contact Form
Questions > Land on website > Message Banners > Info Pages > Contact Form
Contact > Land on website > Clear Telephone / Email Banner > Contact Form

CALL TO ACTION BANNER:
If you need help making your drink the next big brand, speak to us today.

KEYWORDS THAT RELATE TO THE BUSINESS:
brand marketing
drinks marketing
spirits marketing
brand marketing strategy
alcoholic drinks marketing
Drinks Brand Development

LOCATION(S):
United Kingdom -
Worldwide -

Target Market(s)

Male & Female
30-60
Marketing Directors
Brand Developers
Export Directors
Brand Managers

Industry/Entity Type

Marketing

Number of Pages Required

2 pages

Requirements
Must have
• This design will be integrated into wordpress, I have attached a wireframe of what we need, this is NOT a strict guide but contains content that is essential, the wireframes shows the priority of statements and products. the images supplied need to sell the products and services.
The main banner will eventually be animated so this needs to be taken into account.
The cliemt has supplied images which will need to be used in the design , however if you feel you have better images in the same style then they can be used.
Nice to have
• animation included, Jquery
Should not have
• NO fully flash sites or designs, this site will be Search engine optimised and updateable

```html
<!DOCTYPE html>
<html lang="en">
<head>
<meta charset="utf-8">
<title>Proof &amp; Palate – drinks brand marketing</title>
<link rel="stylesheet" href="https://fonts.googleapis.com/css2?family=Noto+Sans:wght@400;700&display=swap">
<style>
:root{
  --blue:#1fa6d8;
  --blue-deep:#2596c8;
  --blue-light:#3fc6e6;
  --page:#f5fbfe;
  --grey-band:#e4e4e4;
  --text:#333;
  --nav-text:#4d5a62;
  --rule:#cfcfcf;
  --yellow:#f2e600;
}
*{margin:0;padding:0;box-sizing:border-box}
html,body{width:1200px;height:581px;overflow:hidden;background:#fff;font-family:"Noto Sans",sans-serif;color:var(--text)}
.sheet{position:absolute;width:544px;background:var(--page)}
.sheet--home{left:28px;top:31px;height:409px}
.sheet--about{left:625px;top:31px;height:520px}

/* header */
.social{position:absolute;left:22px;top:2px;width:106px;height:17px;border-radius:0 0 4px 4px;background:linear-gradient(#f3f3f3,#dcdcdc);display:flex;align-items:center;gap:6px;padding-left:5px;font-size:5.5px;color:#555}
.social span{display:flex;align-items:center;gap:3px;text-decoration:underline}
.social i{display:block;width:10px;height:10px;border-radius:2px;background:var(--blue)}
.social .sep{width:1px;height:11px;background:#bbb}
.brand{position:absolute;left:222px;top:22px;width:100px;display:flex;align-items:center;justify-content:center;gap:4px;font-size:8px;color:var(--blue)}
.brand b{display:block;width:8px;height:8px;border-radius:50%;background:var(--blue)}
.contact{position:absolute;right:22px;top:3px;text-align:right;font-size:7px;line-height:9.5px;color:#444}
.contact em{font-style:normal;color:var(--blue)}
.search{position:absolute;left:404px;top:38px;width:104px;height:13px;border-radius:7px;background:linear-gradient(#e2e2e2,#f4f4f4);box-shadow:inset 0 1px 2px rgba(0,0,0,.15)}
.search-icon{position:absolute;left:512px;top:39px}

/* nav */
.nav{position:absolute;left:0;top:62px;width:544px;height:34px;background:linear-gradient(90deg,var(--blue-deep),var(--blue-light))}
.nav a{position:absolute;top:5px;font-size:9.5px;line-height:11.5px;color:var(--nav-text);text-decoration:none}
.nav a.is-active{color:#fff}
.nav a.home{font-size:10.5px}
.nav .divider{position:absolute;top:4px;width:1px;height:26px;background:rgba(255,255,255,.18)}

/* slider */
.slider{position:absolute;left:22px;top:101px;width:500px;height:144px;background:#3a8fa6;overflow:hidden}
.slider .photo{position:absolute;left:27px;top:0;width:447px;height:144px;background:linear-gradient(120deg,#5c6277 0%,#8a8ea8 30%,#4d5a7a 55%,#a89a6a 80%,#6e7486 100%)}
.slider .quote{position:absolute;left:242px;top:18px;width:206px;height:109px;background:rgba(22,166,220,.92);color:#fff;text-align:right;padding:15px 8px 0 0}
.quote p{font-size:16px;line-height:16.5px;letter-spacing:.3px}
.quote cite{display:block;font-style:normal;font-size:6.5px;line-height:7px;color:var(--yellow);margin-top:11px;font-weight:700}
.arrow{position:absolute;top:62px;width:19px;height:19px;border-radius:50%;background:#fff}
.arrow svg{display:block}

/* feature band */
.features{position:absolute;left:0;width:544px;height:112px;background:var(--grey-band)}
.sheet--home .features{top:252px}
.sheet--about .features{top:357px}
.feature{position:absolute;top:15px;width:150px}
.feature h3{font-weight:400;font-size:11px;line-height:12.6px;color:var(--blue)}
.feature hr{border:0;height:1px;background:linear-gradient(90deg,var(--rule),transparent);margin:7px 0 8px}
.feature p{width:136px;font-size:5.8px;line-height:9.3px;letter-spacing:.2px;color:#333}
.feature .more{display:flex;align-items:center;gap:4px;margin-top:3px;font-size:5px;color:var(--blue);text-decoration:underline}
.feature .more i{display:block;width:8px;height:8px;border:1px solid var(--blue);border-radius:50%}

/* footer */
.footer{position:absolute;left:0;width:544px;text-align:center;font-size:4.8px;line-height:6px}
.sheet--home .footer{top:374px}
.sheet--about .footer{top:479px}
.footer .keywords{color:var(--blue)}
.footer .keywords b{color:#333;font-weight:400}
.footer .legal{margin-top:8px;color:#333}
.footer .legal span{color:var(--blue)}

/* about content */
.page-title{position:absolute;left:21px;top:106px;font-weight:400;font-size:14.5px;line-height:18px;letter-spacing:.6px;color:var(--blue)}
.copy{position:absolute;left:21px;top:146px;width:305px;font-size:6.3px;line-height:7.6px;color:#333;letter-spacing:.33px}
.copy p+p{margin-top:7.5px}
.gallery-item{position:absolute;left:336px;width:186px}
.gallery-item--martini{top:105px;height:144px;background:linear-gradient(160deg,#7c8eb0 0%,#b9c6d8 45%,#5c6f96 100%)}
.gallery-item--bar{top:254px;height:94px;background:linear-gradient(110deg,#1d2a4e 0%,#5a4b6c 40%,#8a5a3a 75%,#2c2a40 100%)}
</style>
</head>
<body>

<!-- home page -->
<section class="sheet sheet--home">
  <div class="social"><span><i></i>Chirpline</span><em class="sep"></em><span><i></i>Pagebook</span></div>
  <div class="brand"><b></b>Proof &amp; Palate</div>
  <div class="contact"><em>t:</em> 020 7946 0318<br><em>e:</em> info@proofandpalate.com</div>
  <div class="search"></div>
  <svg class="search-icon" width="10" height="10" viewBox="0 0 10 10"><circle cx="4" cy="4" r="3" fill="none" stroke="#1fa6d8" stroke-width="1.3"/><line x1="6.2" y1="6.2" x2="9" y2="9" stroke="#1fa6d8" stroke-width="1.6"/></svg>

  <nav class="nav">
    <a class="home is-active" style="left:22px">home<br>page</a>
    <span class="divider" style="left:66px"></span>
    <a style="left:81px">what<br>we do</a>
    <span class="divider" style="left:140px"></span>
    <a style="left:163px">a little bit<br>about us</a>
    <span class="divider" style="left:222px"></span>
    <a style="left:248px">our spirit<br>marketing</a>
    <span class="divider" style="left:312px"></span>
    <a style="left:338px">big brand<br>success</a>
    <span class="divider" style="left:400px"></span>
    <a style="left:426px">our<br>blog</a>
    <span class="divider" style="left:465px"></span>
    <a style="left:486px">speak<br>to us</a>
  </nav>

  <div class="slider">
    <div class="photo" role="img" aria-label="Close-up photograph of a martini glass with an olive"></div>
    <div class="quote">
      <p>“turning our small<br>time whisky into a<br>national brand”</p>
      <cite>Dan Whitcombe<br>Halden Spirits</cite>
    </div>
    <span class="arrow" style="left:4px"><svg width="19" height="19" viewBox="0 0 19 19"><polyline points="11,5 7,9.5 11,14" fill="none" stroke="#2596c8" stroke-width="2"/></svg></span>
    <span class="arrow" style="left:477px"><svg width="19" height="19" viewBox="0 0 19 19"><polyline points="8,5 12,9.5 8,14" fill="none" stroke="#2596c8" stroke-width="2"/></svg></span>
  </div>

  <div class="features">
    <div class="feature" style="left:39px"><h3>22 years experience<br>with big brands</h3><hr><p>Gismod, mauris vel biben du mfturingilla, fringilla, metutus dui vi fringilla, a artucu, vitae eleiffringilla.</p><span class="more"><i></i>read more</span></div>
    <div class="feature" style="left:203px"><h3>Making your drink<br>the next big brand</h3><hr><p>Gismod, mauris vel biben du mfturingilla, fringilla, metutus dui vi fringilla, a artucu, vitae eleiffringilla.</p><span class="more"><i></i>read more</span></div>
    <div class="feature" style="left:368px"><h3>350 outlets that<br>listen to what we say</h3><hr><p>Gismod, mauris vel biben du mfturingilla, fringilla, metutus dui vi fringilla, a artucu, vitae eleiffringilla.</p><span class="more"><i></i>read more</span></div>
  </div>

  <footer class="footer">
    <div class="keywords">brand marketing <b>|</b> brand marketing strategy <b>|</b> drinks marketing <b>|</b> spirits marketing <b>|</b> alcoholic drinks marketing <b>|</b> drinks brand development</div>
    <div class="legal">© 1999-2010 Proof &amp; Palate &nbsp;| <span>terms and conditions</span> | <span>privacy policy</span></div>
  </footer>
</section>

<!-- about page -->
<section class="sheet sheet--about">
  <div class="social"><span><i></i>Chirpline</span><em class="sep"></em><span><i></i>Pagebook</span></div>
  <div class="brand"><b></b>Proof &amp; Palate</div>
  <div class="contact"><em>t:</em> 020 7946 0318<br><em>e:</em> info@proofandpalate.com</div>
  <div class="search"></div>
  <svg class="search-icon" width="10" height="10" viewBox="0 0 10 10"><circle cx="4" cy="4" r="3" fill="none" stroke="#1fa6d8" stroke-width="1.3"/><line x1="6.2" y1="6.2" x2="9" y2="9" stroke="#1fa6d8" stroke-width="1.6"/></svg>

  <nav class="nav">
    <a class="home" style="left:22px">home<br>page</a>
    <span class="divider" style="left:66px"></span>
    <a style="left:81px">what<br>we do</a>
    <span class="divider" style="left:140px"></span>
    <a class="is-active" style="left:163px">a little bit<br>about us</a>
    <span class="divider" style="left:222px"></span>
    <a style="left:248px">our spirit<br>marketing</a>
    <span class="divider" style="left:312px"></span>
    <a style="left:338px">big brand<br>success</a>
    <span class="divider" style="left:400px"></span>
    <a style="left:426px">our<br>blog</a>
    <span class="divider" style="left:465px"></span>
    <a style="left:486px">speak<br>to us</a>
  </nav>

  <h1 class="page-title">a little bit about us</h1>
  <div class="copy">
    <p>Lorem ipsum dolor sit amet, consectetur adipiscing elit. Nulla cursus dignissim eleifend. Etiam suscipit urna non dui blandit molestie. Aliquam at felis a felis tincidunt tempor. In tempor, ipsum eu semper luctus, orci ipsum tempor libero, id vestibulum massa nunc in risus. Aliquam condimentum rhoncus vehicula. Ut tristique elementum sapien non accumsan. Nulla convallis elit quam, eu pellentesque risus. Suspendisse non nibh lorem. Nam porta tellus eu arcu tempus suscipit ultrices ligula ultricies. Aenean pretium accumsan aliquam. Nunc a enim felis, quis eleifend mi. In volutpat vulputate arcu, in lobortis nulla rutrum in. Integer a risus eu dolor faucibus hendrerit. Sed elementum, odio at placerat elementum, urna quam sagittis enim, sit amet blandit mi arcu et est. Nam congue blandit quam, at blandit arcu consectetur eu. Sed congue tristique augue, at pellentesque lectus mattis in. Mauris pulvinar tempus odio, id fringilla tortor blandit sed. Nam vel eros vel nibh dignissim hendrerit.</p>
    <p>Vivamus et adipiscing mauris. Praesent porttitor nisi sollicitudin purus pharetra eget ullamcorper nunc convallis. Maecenas porta luctus orci sed auctor. Donec sit amet est leo. Nam a ligula orci. Mauris at pulvinar mi. Praesent pretium nisi eu ligula faucibus dictum. Quisque commodo imperdiet elit, a vulputate sapien commodo at. Donec et dolor ut sapien posuere viverra. Vivamus euismod semper urna, viverra cursus odio mollis eu. Nam magna metus, aliquam eu pharetra vitae, blandit malesuada magna. Integer vitae diam ac augue rhoncus convallis. Nam id lacus sed mi ullamcorper venenatis quis sed ante. Morbi id ligula mi, sed porttitor ligula. Mauris hendrerit, ligula a aliquet vehicula, mi nulla tempus elit, vitae commodo leo dui a est. Aenean eu dui orci. Phasellus ullamcorper leo eget mauris ultrices hendrerit. Ut ultricies viverra diam, ut hendrerit nulla ultrices id.</p>
  </div>
  <div class="gallery-item gallery-item--martini" role="img" aria-label="Photograph of a martini glass with an olive"></div>
  <div class="gallery-item gallery-item--bar" role="img" aria-label="Photograph of a cocktail on a busy bar counter"></div>

  <div class="features">
    <div class="feature" style="left:39px"><h3>22 years experience<br>with big brands</h3><hr><p>Gismod, mauris vel biben du mfturingilla, fringilla, metutus dui vi fringilla, a artucu, vitae eleiffringilla.</p><span class="more"><i></i>read more</span></div>
    <div class="feature" style="left:203px"><h3>Making your drink<br>the next big brand</h3><hr><p>Gismod, mauris vel biben du mfturingilla, fringilla, metutus dui vi fringilla, a artucu, vitae eleiffringilla.</p><span class="more"><i></i>read more</span></div>
    <div class="feature" style="left:368px"><h3>350 outlets that<br>listen to what we say</h3><hr><p>Gismod, mauris vel biben du mfturingilla, fringilla, metutus dui vi fringilla, a artucu, vitae eleiffringilla.</p><span class="more"><i></i>read more</span></div>
  </div>

  <footer class="footer">
    <div class="keywords">brand marketing <b>|</b> brand marketing strategy <b>|</b> drinks marketing <b>|</b> spirits marketing <b>|</b> alcoholic drinks marketing <b>|</b> drinks brand development</div>
    <div class="legal">© 1999-2010 Proof &amp; Palate &nbsp;| <span>terms and conditions</span> | <span>privacy policy</span></div>
  </footer>
</section>

</body>
</html>
```